Ardenwell Building and Property Services needs a business card design

We need a business card design for our building and property services business. We already have a logo we just need a creative design and layout on a business card. Emphasis on clean, modern, professional.
Our client targets are mainly body corporates, building managers, construction managers.
We are a building services company that lean more to structural repair of buildings, through concrete rectification and carbon fibre strengthening.
We also refurbish facades, rendering, painting etc
We target higher end body corporates in prestigious locations, hence why we'd like our cards to reflect professionalism, strength, efficiency

Target Market(s)

body corporates, building managers, construction managers

Industry/Entity Type

Construction

Contact Information for Business Card

Ardenwell is the main word, with 'Building and Property Services' underneath.
Level 17, 82 Harlow Street
MERRIDALE
Melbourne
Vic 3094
T: 9518 2736
Duncan Ferris - Director
dunardenwell@mailbox-example.com

Requirements
Must have
• Stand out on the back of the card- strong/ bold, company logo
• All of the contact details written above
Should not have
• I'd like the card to stand out, especially on the back. Id like the company logo to be prominent, although feel free to be creative around it. But remain clean and professional

```html
<!DOCTYPE html>
<html lang="en">
<head>
<meta charset="utf-8">
<title>Ardenwell Building and Property Services – Business Card</title>
<link href="https://fonts.googleapis.com/css2?family=Open+Sans:wght@400;600;700&display=swap" rel="stylesheet">
<style>
  :root {
    --page: #e9e9eb;
    --card: #000000;
    --accent: #1e9be0;
    --text: #ffffff;
    --muted: #b9c3cc;
    --glow: #1f3447;
  }
  * { margin: 0; padding: 0; box-sizing: border-box; }
  html, body { width: 1200px; height: 900px; overflow: hidden; }
  body {
    background: var(--page);
    font-family: "Open Sans", Arial, sans-serif;
    position: relative;
  }
  .card {
    position: absolute;
    background: var(--card);
    color: var(--text);
    overflow: hidden;
  }
  .card--front { left: 238px; top: 62px; width: 554px; height: 342px; }
  .card--back {
    left: 458px; top: 518px; width: 558px; height: 343px;
    background: radial-gradient(circle at 50% 40%, var(--glow) 0%, var(--card) 48%);
  }
  .person {
    position: absolute; top: 30px; left: 0; width: 100%;
    text-align: center;
  }
  .person__name { color: var(--accent); font-size: 19px; font-weight: 600; line-height: 1.2; }
  .person__role { font-size: 13px; margin-top: 2px; }
  .contact {
    position: absolute; left: 26px; top: 63px;
    list-style: none; font-size: 13.5px; line-height: 21px;
  }
  .contact li { display: flex; align-items: center; gap: 9px; }
  .contact svg { width: 11px; height: 11px; fill: var(--accent); flex: none; }
  .address {
    position: absolute; right: 22px; top: 62px;
    text-align: right; font-style: normal; font-size: 14px; line-height: 23px;
  }
  .front-name {
    position: absolute; left: 0; width: 100%; top: 188px;
    text-align: center; color: var(--accent);
    font-size: 68px; font-weight: 700; letter-spacing: 3px;
    text-transform: uppercase; line-height: 1;
  }
  .front-rule {
    position: absolute; left: 0; bottom: 0; width: 100%; height: 5px;
    background: var(--accent);
  }
  .brand {
    position: absolute; left: 0; width: 100%; top: 96px;
    display: flex; flex-direction: column; align-items: center;
  }
  .brand__mark {
    display: flex; align-items: center; gap: 16px;
  }
  .brand__square {
    width: 46px; height: 46px; background: var(--accent); flex: none;
  }
  .brand__name {
    color: var(--accent); font-size: 60px; font-weight: 700;
    letter-spacing: 4px; text-transform: uppercase; line-height: 1;
  }
  .brand__tagline {
    color: var(--muted); font-size: 12px; font-weight: 600;
    letter-spacing: 2.4px; text-transform: uppercase; margin-top: 22px;
  }
</style>
</head>
<body>
  <section class="card card--front">
    <div class="person">
      <p class="person__name">Duncan Ferris</p>
      <p class="person__role">Director</p>
    </div>
    <ul class="contact">
      <li>
        <svg viewBox="0 0 24 24" aria-hidden="true"><path d="M6.6 10.8a15.1 15.1 0 0 0 6.6 6.6l2.2-2.2a1 1 0 0 1 1-.25 11.4 11.4 0 0 0 3.6.57 1 1 0 0 1 1 1V20a1 1 0 0 1-1 1A17 17 0 0 1 3 4a1 1 0 0 1 1-1h3.5a1 1 0 0 1 1 1c0 1.25.2 2.45.57 3.57a1 1 0 0 1-.25 1z"/></svg>
        <span>9518 2736</span>
      </li>
      <li>
        <svg viewBox="0 0 24 24" aria-hidden="true"><path d="M2 5h20v14H2z M3 6l9 7 9-7" /></svg>
        <span>dunardenwell@mailbox-example.com</span>
      </li>
    </ul>
    <address class="address">
      Level 17, 82 Harlow Street<br>
      MERRIDALE<br>
      Melbourne Vic 3094
    </address>
    <p class="front-name">Ardenwell</p>
    <div class="front-rule"></div>
  </section>

  <section class="card card--back">
    <div class="brand">
      <div class="brand__mark">
        <span class="brand__square" aria-hidden="true"></span>
        <p class="brand__name">Ardenwell</p>
      </div>
      <p class="brand__tagline">Building and Property Services</p>
    </div>
  </section>
</body>
</html>
```